Doctors Office Web Design

Name of the business is Lin-Yue Hart M.D.
We need a web design that is attractive for women that want to see Dr. Lin-Yue Hart for Obstetrician Gynecology and Pregnancy care. Dr. Hart earned her degree from Carrow Ridge Medical College of obstetrician gynecology. We want to attract women of child bearing ages to come to our offices for health, education, and pregnancies.

Please visit http://www.drhartclinicweb.com/ to help you get a feel for who we are. We will be adding some pictures and logo in the next few days.

We are looking for to have pages for and tabs including
About Us- History, Our Staff, Dr. Hart
Patient Information- Appointments, E-Prescriptions, Payments Accepted, Insurance
Health- General, Sexual, Mental, Affiliates
Pregnancy- Minimally invasive surgery(our specialty), 4-D Ultra Sound, Hospital Affiliations
Media- News,Pictures, Videos
Locations- Palmer Office, Westvale Office

The colors we would like to use are pastel colors, magenta, and plum

Target Market(s)

Women of all ages with an emphasis on 25-65 year olds

Industry/Entity Type

Business

Requirements
Must have
• Needs to include a location for a our videos and pictures that I will submit shortly. We also want a map to our location or atleast a place for one.
Nice to have
• A place for a google map of our office locations.

```html
<!DOCTYPE html>
<html lang="en">
<head>
<meta charset="utf-8">
<title>Lin-Yue Hart M.D. – Obstetrician/Gynecologist</title>
<link rel="stylesheet" href="https://fonts.googleapis.com/css2?family=Arimo:wght@400;700&family=Cabin+Condensed:wght@500;600&display=swap">
<style>
:root{
  --plum-dark:#5a0c3c;
  --plum:#7d1553;
  --magenta:#9c2370;
  --magenta-light:#b8418c;
  --cream:#f6e7b0;
  --ink:#222;
  --panel-bg:#f4f4f4;
  --panel-line:#cfcfcf;
  --white:#fff;
}
*{box-sizing:border-box;margin:0;padding:0}
html,body{width:857px;height:1200px;overflow:hidden}
body{position:relative;background:var(--white);font-family:Arimo,Arial,sans-serif;color:var(--ink)}
.abs{position:absolute}

.site-header{left:0;top:0;width:857px;height:100px;background:linear-gradient(180deg,#8a1860 0%,#a12a74 60%,#8c1a62 100%)}
.brand-name{left:0;width:790px;top:22px;text-align:center;font-family:Arimo,Arial,sans-serif;font-size:39px;color:#f3e6ee;letter-spacing:.5px}
.brand-tagline{left:0;width:780px;top:76px;text-align:center;font-size:12px;color:var(--white)}
.login-label{left:687px;top:17px;font-size:13px;color:var(--white)}
.login-input{left:681px;top:42px;width:119px;height:22px;background:var(--white);border:1px solid #ddd}
.go-btn{background:var(--magenta);color:var(--white);font-size:11px;text-align:center;border-radius:2px}
.login-go{left:810px;top:42px;width:33px;height:22px;line-height:22px}

.main-nav{left:0;top:100px;width:857px;height:48px;background:linear-gradient(180deg,#6d0f48,#561039);display:flex;align-items:center;padding-left:30px}
.main-nav a{color:var(--white);text-decoration:none;font-size:12.5px;margin-right:26px;padding:7px 8px}
.main-nav a.current{background:var(--magenta);}

.calendar-panel{left:0;top:148px;width:330px;height:278px;background:linear-gradient(180deg,#8e1c64,#7a1455)}
.calendar-title{left:37px;top:190px;font-family:"Cabin Condensed",Arial,sans-serif;font-weight:600;font-size:27px;color:var(--cream)}
.calendar-sub{left:46px;top:240px;font-family:"Cabin Condensed",Arial,sans-serif;font-weight:600;font-size:19px;color:var(--white)}
.date-box{left:24px;top:283px;width:271px;height:113px;background:var(--magenta);border-radius:3px}
.date-field{top:306px;width:61px;height:26px;background:var(--white);border:2px solid #c1541b;border-radius:5px;font-size:11px;color:#b1402b;text-align:center;line-height:22px;font-family:"Cabin Condensed",Arial,sans-serif}
.submit-btn{left:119px;top:348px;width:61px;height:28px;border:1px solid #d277aa;border-radius:5px;background:var(--plum);color:var(--white);font-size:11px;text-align:center;line-height:26px}
.learn-more{left:0;top:425px;width:330px;height:43px;background:var(--plum-dark);color:var(--white);font-family:"Cabin Condensed",Arial,sans-serif;font-weight:600;font-size:20px;display:flex;align-items:center;justify-content:center;gap:8px}

.hero-photo{left:330px;top:148px;width:527px;height:320px;background:linear-gradient(135deg,#f2ece8 0%,#e7dedb 50%,#b9b6b8 100%)}
.hero-copy{left:346px;top:178px;font-family:"Cabin Condensed",Arial,sans-serif;font-weight:600;font-size:16px;line-height:34.5px;color:#6d1140}
.hero-arrow{top:296px}

.side-panel{left:13px;width:272px;background:var(--panel-bg);border:1px solid var(--panel-line);border-radius:4px}
.side-title{width:100%;text-align:center;font-family:"Cabin Condensed",Arial,sans-serif;font-weight:500;font-size:19px;color:#5b0d3b}
.search-input{left:24px;top:518px;width:202px;height:30px;background:var(--white);border:1px solid #bbb;border-radius:5px}
.search-go{left:234px;top:524px;width:32px;height:22px;line-height:22px}
.map-area{left:39px;top:610px;width:223px;height:258px;background:linear-gradient(160deg,#eef0e6,#e3e6da 60%,#c8d3e0);border:1px solid #bbb}
.map-caption{left:13px;width:272px;top:880px;text-align:center;font-size:15px}

.badge{left:58px;top:952px;width:44px;height:64px;border-radius:50%;background:linear-gradient(180deg,#c8a6d6,#4d2a6b)}
.share-block{left:141px;top:933px}
.share-label{font-size:11px;color:#888;}
.share-item{display:flex;align-items:center;gap:6px;font-size:13.5px;margin-top:4px;height:28px}
.share-divider{width:140px;border-top:1px solid #888;margin:6px 0 4px}

.locations-box{left:303px;top:482px;width:540px;height:168px;background:linear-gradient(180deg,#b8468c,#8e1c64);border:2px solid #6d0f48;border-radius:5px}
.tab-title{height:28px;background:var(--magenta-light);color:var(--white);font-size:16px;line-height:28px;border-radius:3px}
.address{font-size:10.5px;line-height:18px;color:var(--white)}
.hours{left:656px;top:542px;font-size:12.5px;line-height:21px;color:var(--white)}
.divider-v{left:628px;top:535px;height:100px;border-left:1px solid #c57aa7}

.photo-strip{top:670px;height:138px}
.strip-frame{left:305px;top:670px;width:540px;height:138px;border:2px solid #b2301a}

.welcome{left:320px;top:822px;width:510px;font-size:10.3px;line-height:20.8px;color:var(--ink)}
.welcome p{margin-bottom:21px}

.site-footer{left:0;top:1150px;width:857px;height:50px;background:linear-gradient(180deg,#8a1860,#6c0f48);color:var(--white);font-size:11px;text-align:center}
.footer-links{padding-top:8px}
.footer-links span{margin:0 12px}
.copyright{margin-top:10px}
</style>
</head>
<body>

<header class="abs site-header">
</header>
<div class="abs brand-name">Lin-Yue Hart M.D.</div>
<div class="abs brand-tagline">Obstetrician/Gynecologist</div>
<div class="abs login-label">Patient Online Login</div>
<div class="abs login-input"></div>
<div class="abs go-btn login-go">Go</div>

<nav class="abs main-nav">
  <a class="current">HOME</a><a>ABOUT US</a><a>PATIENT INFORMATION</a><a>HEALTH</a><a>PREGNANCY</a><a>MEDIA</a><a>LOCATIONS</a><a>CONTACT US</a>
</nav>

<section class="abs calendar-panel"></section>
<h2 class="abs calendar-title">Pregnancy Calendar</h2>
<div class="abs calendar-sub">Enter Your Due Date :</div>
<div class="abs date-box"></div>
<div class="abs date-field" style="left:56px">Month</div>
<div class="abs date-field" style="left:136px">Day</div>
<div class="abs date-field" style="left:213px">Year</div>
<div class="abs submit-btn">&gt; Submit</div>
<div class="abs learn-more">
  <svg width="14" height="14" viewBox="0 0 14 14"><circle cx="7" cy="7" r="7" fill="#fff"/><path d="M3.5 5.5 7 9 10.5 5.5" fill="none" stroke="#5a0c3c" stroke-width="2"/></svg>
  Learn more
</div>

<div class="abs hero-photo" role="img" aria-label="Photo of a smiling pregnant woman relaxing with a bowl of fruit"></div>
<div class="abs hero-copy">Serving All Areas of Women's Health, including:<br>Obstetrics, Family Planning, Hormonal Evaluation,<br>Incontinence, Infertility, and Gynecology Surgery</div>
<svg class="abs hero-arrow" style="left:336px" width="28" height="30" viewBox="0 0 28 30"><path d="M24 2 6 15 24 28 18 15Z" fill="#6d1140"/></svg>
<svg class="abs hero-arrow" style="left:824px" width="28" height="30" viewBox="0 0 28 30"><path d="M4 2 22 15 4 28 10 15Z" fill="#6d1140"/></svg>

<section class="abs side-panel" style="top:480px;height:86px">
  <h3 class="side-title" style="margin-top:9px">Search</h3>
</section>
<div class="abs search-input"></div>
<div class="abs go-btn search-go">Go</div>

<section class="abs side-panel" style="top:575px;height:335px">
  <h3 class="side-title" style="margin-top:8px">Directions</h3>
</section>
<div class="abs map-area" role="img" aria-label="Map showing the office location"></div>
<div class="abs map-caption">Dr. Lin-Yue Hart's</div>

<div class="abs badge" role="img" aria-label="Awareness month badge"></div>
<div class="abs share-block">
  <div class="share-label">Contact Business</div>
  <div class="share-item"><svg width="26" height="26" viewBox="0 0 26 26"><circle cx="13" cy="12" r="11" fill="#3f7fcf"/><rect x="12" y="6" width="2.5" height="8" fill="#fff"/><rect x="12" y="16" width="2.5" height="2.5" fill="#fff"/></svg>By email</div>
  <div class="share-item" style="margin-top:10px"><svg width="26" height="22" viewBox="0 0 26 22"><rect x="1" y="3" width="24" height="17" fill="#eef0f4" stroke="#8a93a4"/><path d="M1 3 13 13 25 3" fill="none" stroke="#8a93a4"/></svg>Email me this info</div>
  <div class="share-divider"></div>
  <div class="share-label">Share</div>
  <div class="share-item"><svg width="26" height="24" viewBox="0 0 26 24"><rect x="1" y="7" width="24" height="16" fill="#eef0f4" stroke="#8a93a4"/><path d="M1 7 13 16 25 7" fill="none" stroke="#8a93a4"/></svg>Email to a friend</div>
  <div class="share-item"><svg width="26" height="26"><rect width="26" height="26" fill="#3b5998"/></svg>Friendly</div>
  <div class="share-item"><svg width="26" height="26"><rect width="26" height="26" fill="#6cc5e3"/></svg>Chirper</div>
</div>

<section class="abs locations-box"></section>
<div class="abs tab-title" style="left:318px;top:493px;width:145px;padding-left:14px">Our Locations</div>
<div class="abs tab-title" style="left:644px;top:492px;width:193px;padding-left:16px">Schedule Appointments</div>
<div class="abs address" style="left:314px;top:538px">2210 Harbor Crest Avenue<br>Suite 115-116<br>Westvale, Florida&nbsp; 33400<br>Tel:&nbsp; (555) 210-4400<br>Fax: (555) 210-4411</div>
<div class="abs address" style="left:488px;top:536px">480 N.W. 9th Street<br>Suite 110A<br>Palmer, Florida&nbsp; 33480<br>Tel:&nbsp; (555) 318-2090<br>Fax:&nbsp; (555) 318-2091</div>
<div class="abs divider-v"></div>
<div class="abs hours">Hours: M–F, 8:30 a.m. to 5 p.m.<br>Phone: (555) 210-4400</div>

<div class="abs photo-strip" style="left:305px;width:189px;background:linear-gradient(180deg,#d8b58c,#b88b63)" role="img" aria-label="Photo of a smiling woman"></div>
<div class="abs photo-strip" style="left:494px;width:205px;background:linear-gradient(180deg,#e2e6ea,#a9b4bd)" role="img" aria-label="Photo of an ultrasound examination"></div>
<div class="abs photo-strip" style="left:699px;width:146px;background:linear-gradient(180deg,#c9cdd2,#7f9aa0)" role="img" aria-label="Photo of a doctor with a stethoscope"></div>
<div class="abs strip-frame"></div>

<main class="abs welcome">
  <p>Welcome to Dr. Lin-Yue Hart's website. Here you will be able to find information about both of our offices, meet Dr. Hart and her staff, and browse through our women's health links to learn&nbsp; more about pregnancy, nutrition,&nbsp; exercise, and other women's health issues. Have fun and if you have any questions, feel free to contact us at drhart@lymail.net</p>
  <p>Obstetrics and Gynecology / Reproductive Endocrinology and Infertility: Recurrent Pregnancy Loss (Recurrent Miscarriage)Recurrent pregnancy loss - also known as recurrent miscarriage - is medically defined as the loss of three or more pregnancies within the first 20 weeks of gestation. However, many patients seeking treatment for recurrent pregnancy loss at Linden Vale School of Medicine often consult one of the school's physician specialists in reproductive endocrinology after experiencing two miscarriages.</p>
  <p style="margin-bottom:0">FOR AN APPOINTMENT, CALL 555-286-0100, extension 1.<br>Patients may be referred by their primary care physician or obstetrician/gynecologist or may be self-referred. area to provide assistive reproductive treatment using in vitro methods. Personal case studies and information on what to expect can be found at their web site.</p>
</main>

<footer class="abs site-footer">
  <div class="footer-links">Privacy Policy<span>|</span>Terms &amp; Conditions<span>|</span>Contact Us</div>
  <div class="copyright">Copyright ©&nbsp; Lin-Yue Hart M.D., All Rights Reserved</div>
</footer>

</body>
</html>
```